The Amber Lantern illustrated story adaptation design

I need a graphic-novel-style design of the 10-page story, “The Amber Lantern.” This will appear in a collection of graphic-novel-style adaptations of stories which I am posting online (and printing) in May.

Half of the files are on filecrate (under "6 images"):

https://www.filecrate-share.net/s/q3mz81kd0tx5pw2/page%20thumbs_0full_01.jpg?dl=0

Target Market(s)

comic book readers, graphic novel readers, young adult readers

Industry/Entity Type

Publishing

Font styles to use
Serif
Other font styles liked:
• Caslon Anitque, Californian FB, 1584 Pragmatica Lima

Colors

Designer to choose colors to be used in the design.

Requirements
Must have
• A bold design scheme !! The art and text are solid, but they certainly need a clever design concept that can bind the project together.
Nice to have
• An inviting, reader-friendly background of some kind (I offer suggestions in my notes).
Should not have
• Hard-to-read graphics

```html
<!DOCTYPE html>
<html lang="en">
<head>
<meta charset="utf-8">
<title>The Amber Lantern — Page</title>
<link href="https://fonts.googleapis.com/css2?family=Marcellus&family=Cormorant+Garamond:ital,wght@1,700&display=swap" rel="stylesheet">
<style>
  :root {
    --ink: #161c22;
    --ink-deep: #10151a;
    --acid: #e1e40c;
    --speck: #1a2026;
  }
  html, body {
    margin: 0;
    padding: 0;
    width: 954px;
    height: 1200px;
    overflow: hidden;
    background: var(--ink);
  }
  .page {
    position: relative;
    width: 954px;
    height: 1200px;
    overflow: hidden;
    background: var(--ink);
  }
  .page-art {
    position: absolute;
    inset: 0;
    width: 954px;
    height: 1200px;
  }
  .caption {
    position: absolute;
    margin: 0;
    color: var(--acid);
    font-family: "Marcellus", serif;
    font-weight: 400;
  }
  .caption span { display: block; white-space: nowrap; }
  .title-caption {
    left: 26px;
    top: 4px;
    font-family: "Cormorant Garamond", serif;
    font-style: italic;
    font-weight: 700;
    font-size: 46px;
    line-height: 44px;
    letter-spacing: 5px;
  }
  .title-caption .line-2 { margin-left: -3px; letter-spacing: 5.5px; }
  .omen-caption {
    left: 0;
    top: 22px;
    font-size: 38px;
    line-height: 40px;
    letter-spacing: 1px;
  }
  .mercenary-caption {
    left: 20px;
    top: 349px;
    font-size: 28.5px;
    line-height: 32px;
    letter-spacing: 2.2px;
  }
  .mercenary-caption .indent { margin-left: 47px; }
</style>
</head>
<body>
<main class="page">
  <svg class="page-art" viewBox="0 0 1193 1500" preserveAspectRatio="none">
    <defs>
      <linearGradient id="scene-dusk" x1="0" y1="0" x2="0.3" y2="1">
        <stop offset="0" stop-color="#2a4446"/>
        <stop offset="0.3" stop-color="#3d5e5a"/>
        <stop offset="0.5" stop-color="#283a3e"/>
        <stop offset="0.7" stop-color="#3a4a52"/>
        <stop offset="1" stop-color="#1c282e"/>
      </linearGradient>
      <radialGradient id="dusk-haze" cx="0.35" cy="0.2" r="0.5">
        <stop offset="0" stop-color="#6b8a86" stop-opacity="0.45"/>
        <stop offset="1" stop-color="#6b8a86" stop-opacity="0"/>
      </radialGradient>
      <linearGradient id="scene-temple" x1="0" y1="0" x2="0.4" y2="1">
        <stop offset="0" stop-color="#3a5866"/>
        <stop offset="0.25" stop-color="#2b4458"/>
        <stop offset="0.5" stop-color="#4b5670"/>
        <stop offset="0.75" stop-color="#2a3a48"/>
        <stop offset="1" stop-color="#1a2630"/>
      </linearGradient>
      <radialGradient id="temple-haze" cx="0.7" cy="0.7" r="0.5">
        <stop offset="0" stop-color="#706e8a" stop-opacity="0.45"/>
        <stop offset="1" stop-color="#706e8a" stop-opacity="0"/>
      </radialGradient>
      <linearGradient id="scene-moon" x1="0" y1="0" x2="0.2" y2="1">
        <stop offset="0" stop-color="#5f8c8a"/>
        <stop offset="0.3" stop-color="#426e6e"/>
        <stop offset="0.55" stop-color="#2c4a50"/>
        <stop offset="0.75" stop-color="#3a5258"/>
        <stop offset="1" stop-color="#151f26"/>
      </linearGradient>
      <radialGradient id="moon-haze" cx="0.12" cy="0.1" r="0.4">
        <stop offset="0" stop-color="#b8cccc" stop-opacity="0.4"/>
        <stop offset="1" stop-color="#b8cccc" stop-opacity="0"/>
      </radialGradient>
      <linearGradient id="scene-plaza" x1="0" y1="0" x2="0.3" y2="1">
        <stop offset="0" stop-color="#3f6868"/>
        <stop offset="0.35" stop-color="#2e4c52"/>
        <stop offset="0.6" stop-color="#253642"/>
        <stop offset="1" stop-color="#141b22"/>
      </linearGradient>
      <radialGradient id="plaza-haze" cx="0.6" cy="0.4" r="0.5">
        <stop offset="0" stop-color="#4e5e7a" stop-opacity="0.4"/>
        <stop offset="1" stop-color="#4e5e7a" stop-opacity="0"/>
      </radialGradient>
      <radialGradient id="emblem-glow" cx="0.5" cy="0.5" r="0.6">
        <stop offset="0" stop-color="#5c5e1c"/>
        <stop offset="0.55" stop-color="#2e3420"/>
        <stop offset="1" stop-color="#161c22"/>
      </radialGradient>

      <filter id="paint-grain" x="0" y="0" width="100%" height="100%">
        <feTurbulence type="fractalNoise" baseFrequency="0.012 0.05" numOctaves="3" seed="7" result="noise"/>
        <feColorMatrix in="noise" type="matrix"
          values="0 0 0 0 0.08  0 0 0 0 0.12  0 0 0 0 0.16  2.4 0 0 0 -1.1" result="streaks"/>
        <feComposite in="streaks" in2="SourceGraphic" operator="in" result="shade"/>
        <feMerge><feMergeNode in="SourceGraphic"/><feMergeNode in="shade"/></feMerge>
      </filter>

      <filter id="stipple" x="0" y="0" width="100%" height="100%">
        <feTurbulence type="fractalNoise" baseFrequency="0.9" numOctaves="2" seed="3" result="noise"/>
        <feColorMatrix in="noise" type="matrix"
          values="0 0 0 0 0.1  0 0 0 0 0.12  0 0 0 0 0.14  14 0 0 0 -8.6" result="dots"/>
        <feComposite in="dots" in2="SourceGraphic" operator="in" result="inked"/>
        <feMerge><feMergeNode in="SourceGraphic"/><feMergeNode in="inked"/></feMerge>
      </filter>
    </defs>

    <!-- scene panels -->
    <g class="scenes" filter="url(#paint-grain)">
      <g class="scene scene-ridge" role="img" aria-label="Painted dusk view of a stepped pyramid above dark hills">
        <polygon points="0,0 505,0 668,350 540,480 0,325" fill="url(#scene-dusk)"/>
        <polygon points="0,0 505,0 668,350 540,480 0,325" fill="url(#dusk-haze)"/>
      </g>
      <g class="scene scene-temple" role="img" aria-label="Painted view of a temple complex in blue shadow">
        <polygon points="812,548 1193,552 1193,1030 768,945" fill="url(#scene-temple)"/>
        <polygon points="812,548 1193,552 1193,1030 768,945" fill="url(#temple-haze)"/>
      </g>
      <g class="scene scene-moonrise" role="img" aria-label="Painted night city of pyramids under a pale moon">
        <polygon points="0,1008 400,998 432,1160 612,1135 635,1500 0,1500" fill="url(#scene-moon)"/>
        <polygon points="0,1008 400,998 432,1160 612,1135 635,1500 0,1500" fill="url(#moon-haze)"/>
      </g>
      <g class="scene scene-plaza" role="img" aria-label="Painted dark plaza with temple steps">
        <polygon points="640,1132 722,1085 768,975 1193,1085 1193,1500 662,1500" fill="url(#scene-plaza)"/>
        <polygon points="640,1132 722,1085 768,975 1193,1085 1193,1500 662,1500" fill="url(#plaza-haze)"/>
      </g>
    </g>

    <!-- acid bands -->
    <g class="bands" fill="var(--acid)" filter="url(#stipple)">
      <polygon points="505,0 560,0 710,345 560,505 520,482 665,350"/>
      <polygon points="0,320 540,478 530,520 0,365"/>
      <polygon points="0,980 410,978 412,1010 0,1012"/>
      <polygon points="760,905 1193,1045 1193,1082 758,945"/>
      <polygon points="598,1138 638,1132 668,1500 625,1500"/>
      <polygon points="775,512 1193,508 1193,550 800,555"/>
    </g>

    <!-- emblem frame -->
    <polygon class="emblem-frame" fill="var(--acid)" filter="url(#stipple)"
      points="520,468 790,515 725,1085 428,1165 368,675"/>
    <polygon class="emblem" role="img" aria-label="Carved glyph of a crested bird standing before a temple"
      points="540,512 752,548 712,1055 450,1120 400,690" fill="url(#emblem-glow)"/>
  </svg>

  <h1 class="caption title-caption">
    <span class="line-1">These were</span>
    <span class="line-2">lawless times</span>
  </h1>

  <p class="caption omen-caption">
    <span style="margin-left:509px">The kingdoms of Ek</span>
    <span style="margin-left:526px">were disintegrating.</span>
    <span style="margin-left:542px">The Maya had greatly</span>
    <span style="margin-left:558px">displeased the gods,</span>
    <span style="margin-left:576px">who had punished</span>
    <span style="margin-left:594px">them since the</span>
    <span style="margin-left:588px">Spring, when the</span>
    <span style="margin-left:581px">corn had first gone</span>
    <span style="margin-left:634px">bad.</span>
  </p>

  <p class="caption mercenary-caption">
    <span>The adven-</span>
    <span>turer had left his</span>
    <span>own tribes to serve</span>
    <span>in the emperor’s</span>
    <span>pay.</span>
    <span class="indent">He had been</span>
    <span>satisfied with</span>
    <span>good wage; then</span>
    <span>he lost his taste</span>
    <span>for slaughtering</span>
    <span>farmers and</span>
    <span>peasants.</span>
  </p>
</main>
</body>
</html>
```